Website design for respected, long standing real estate development company in Central Oregon

Uncoded PSD design only. Homepage and one interior sample page.

Updated website design needed for Halvard Holdings, one of Central Oregon’s oldest and most respected real estate development companies. They develop communities that focus on natural beauty and upscale amenities.

They need a website that features their long, unique history and their current efforts to build smart, healthy and livable communities. They need to tell their story to those who aren't familiar with the company. They need to build credibility and set themselves apart from other real estate development companies.

Current site: http://halvard-holdings.example/

Target Market(s)

Target market is people who are new or plan to relocate to Central Oregon and are researching communities they want to live in.
Secondary markets are potential project partners, and the media. They need to build credibility with these audiences.
The site also needs to be easy to use for non-profits seeking contributions.

Industry/Entity Type

Real Estate Development

Number of Pages Required

Font styles to use
Sans Serif

Requirements
Must have
• Must have simple, user-friendly navigation with organized content.
• Design must be fresh, light and modern.
• Design must use great, high impact imagery that promotes the Central Oregon lifestyle.
• Design must highlight current and future communities and encourage click-throughs to those specific websites.
• Include video element.
• Include social links.
• Do not use dummy copy/lorum ipsum. Use copy from the current site instead. Use correct phone number, address, etc.
Should not have
• Lorum ipsum/dummy copy

```html
<!DOCTYPE html>
<html lang="en">
<head>
<meta charset="utf-8">
<title>Halvard Holdings</title>
<link href="https://fonts.googleapis.com/css2?family=Raleway:wght@500;600;700&family=Lato:wght@400;700&display=swap" rel="stylesheet">
<style>
:root{
  --plum:#4a2340;
  --plum-dark:#3d1c35;
  --light:#dcdbd9;
  --ink:#2b2b2b;
  --white:#ffffff;
  --black:#000000;
}
*{margin:0;padding:0;box-sizing:border-box}
html,body{width:777px;height:1200px;overflow:hidden}
body{position:relative;font-family:'Lato',sans-serif;background:var(--black);color:var(--ink)}
.abs{position:absolute}
/* nav */
.topnav{left:0;top:0;width:777px;height:44px;font-size:8px;color:var(--white);z-index:3;border-bottom:1px solid rgba(255,255,255,.15)}
.topnav span{position:absolute;top:0;height:44px;line-height:44px;white-space:nowrap}
.topnav .active{background:var(--plum);padding:0 9px}
/* hero */
.hero{left:0;top:0;width:777px;height:360px;
  background:
    radial-gradient(ellipse 220px 90px at 60px 150px,rgba(150,160,175,.55),transparent 70%),
    radial-gradient(ellipse 260px 160px at 560px 210px,rgba(95,90,70,.45),transparent 70%),
    linear-gradient(180deg,#4d5346 0%,#3a4330 30%,#2f3a26 55%,#3d3b2e 80%,#55534a 100%)}
.brand-tab{left:218px;top:43px;z-index:3}
.brand-name{left:260px;top:64px;z-index:4;font-family:'Raleway',sans-serif;font-weight:600;font-size:14px;color:var(--plum);display:flex;align-items:center;gap:7px;white-space:nowrap}
.brand-name i{display:block;width:22px;height:22px;background:var(--plum)}
.hero-title{left:0;width:777px;top:194px;text-align:center;font-family:'Raleway',sans-serif;font-weight:600;font-size:40px;color:var(--white);letter-spacing:.5px}
/* communities */
.communities{left:0;top:360px;width:777px;height:234px;background:var(--light)}
.community{position:absolute;top:134px;width:180px;text-align:center}
.community h3{font-family:'Raleway',sans-serif;font-weight:700;font-size:9.5px;color:var(--ink);letter-spacing:.2px;white-space:nowrap}
.community h3.current{color:var(--plum)}
.community p{font-size:7.4px;line-height:10.4px;color:#444;margin-top:8px;padding:0 12px}
.community .more{font-size:7.4px;color:#333;margin-top:6px}
/* welcome */
.welcome{left:0;top:594px;width:777px;height:166px;background:var(--plum);text-align:center;color:var(--white)}
.welcome h2{font-family:'Raleway',sans-serif;font-weight:600;font-size:22px;margin-top:35px}
.welcome p{font-size:7.2px;line-height:14.5px;margin:12px auto 0;width:530px;color:#e9dfe6}
.welcome .btn{display:inline-block;margin-top:12px;background:var(--white);color:var(--plum);font-size:8px;width:82px;height:25px;line-height:25px}
/* video */
.video{left:0;top:760px;width:777px;height:213px;background:linear-gradient(100deg,#1d2430 0%,#2a3340 40%,#1a2230 70%,#222a36 100%)}
.video h2{position:absolute;left:94px;top:60px;font-family:'Raleway',sans-serif;font-weight:600;font-size:22px;color:var(--white)}
.video p{position:absolute;left:94px;top:96px;width:370px;font-size:7.4px;line-height:14.6px;color:var(--white)}
.video .btn{position:absolute;left:90px;top:149px;width:99px;height:24px;line-height:24px;text-align:center;background:var(--plum-dark);color:var(--white);font-family:'Raleway',sans-serif;font-size:10.5px;font-weight:500}
.play{left:506px;top:846px}
/* recent */
.recent{left:0;top:973px;width:777px;height:169px;background:var(--black);color:var(--white)}
.recent h2{text-align:center;font-family:'Raleway',sans-serif;font-weight:600;font-size:22px;margin-top:19px}
.post{position:absolute;left:120px;top:67px;width:535px;height:75px;border:1px solid #9a9a9a}
.post-date{position:absolute;left:47px;top:12px;width:60px;height:48px;background:var(--plum);overflow:hidden;text-align:center;font-size:9px;color:var(--white)}
.post-date .m{margin-top:6px}
.post-date .wave{position:absolute;left:0;bottom:0}
.post-date .y{position:absolute;left:0;bottom:3px;width:60px;font-size:11px;color:var(--plum);letter-spacing:.5px}
.post h4{position:absolute;left:120px;top:11px;font-family:'Raleway',sans-serif;font-weight:600;font-size:8.3px;white-space:nowrap}
.post p{position:absolute;left:121px;top:27px;width:380px;font-size:7px;line-height:12px;color:#cfcfcf}
/* footer */
.footer{left:0;top:1142px;width:777px;height:58px;background:var(--plum)}
.footer small{position:absolute;left:34px;top:24px;font-size:6.3px;color:var(--white)}
.social{position:absolute;top:21px;display:flex;gap:12px;left:629px}
.social i{display:block;width:12px;height:12px;border:1.5px solid #cfc3cc;border-radius:50%}
</style>
</head>
<body>

<div class="abs hero" role="img" aria-label="Lifestyle photo of tall pines, a snow-capped Cascade peak and a mountain home in Central Oregon"></div>

<nav class="abs topnav">
  <span class="active" style="left:30px">Home</span>
  <span style="left:95px">Real Estate Developments</span>
  <span style="left:221px">Real Estate Sales</span>
  <span style="left:312px">Maps</span>
  <span style="left:361px">Vacation Rentals</span>
  <span style="left:452px">Property Owner Resources</span>
  <span style="left:583px">About Us</span>
  <span style="left:646px">Contact Us</span>
  <span style="left:718px">Blogs</span>
</nav>

<svg class="abs brand-tab" width="336" height="70" viewBox="0 0 336 70">
  <polygon points="2,0 334,0 326,54 18,70" fill="#efefef"/>
</svg>
<div class="abs brand-name"><i></i>Halvard Holdings Corporation</div>

<h1 class="abs hero-title">HALVARD HOLDINGS</h1>

<section class="abs communities">
  <svg class="abs" style="left:0;top:0" width="777" height="130" viewBox="0 0 777 130">
    <line x1="108" y1="77" x2="661" y2="77" stroke="#ffffff" stroke-width="1.5"/>
    <circle cx="108" cy="77" r="45" fill="#fff" stroke="#4a2340" stroke-width="1.5"/>
    <circle cx="294" cy="77" r="45" fill="#fff"/>
    <circle cx="294" cy="77" r="41" fill="#4a2340"/>
    <circle cx="480" cy="77" r="45" fill="#fff"/>
    <circle cx="480" cy="77" r="41" fill="#4a2340"/>
    <circle cx="661" cy="77" r="45" fill="#fff"/>
    <circle cx="661" cy="77" r="41" fill="#4a2340"/>
    <polygon points="108,57 98,71 103,71 95,82 101,82 93,93 123,93 115,82 121,82 113,71 118,71" fill="#4a2340"/>
    <rect x="105" y="93" width="6" height="5" fill="#4a2340"/>
    <g fill="none" stroke="#fff" stroke-width="3" stroke-linejoin="round">
      <polygon points="294,61 311,69 311,87 294,95 277,87 277,69"/>
      <polyline points="277,69 294,77 311,69"/>
      <line x1="294" y1="77" x2="294" y2="95"/>
    </g>
    <g fill="#fff">
      <polygon points="480,61 496,69 480,77 464,69"/>
      <polygon points="464,75 480,83 496,75 496,80 480,88 464,80"/>
      <polygon points="468,86 480,92 492,86 492,90 480,96 468,90"/>
    </g>
    <g stroke="#fff" stroke-width="3" fill="#fff">
      <line x1="652" y1="86" x2="670" y2="68"/>
      <polygon points="675,63 675,74 664,63" stroke-width="1"/>
      <polygon points="647,91 647,80 658,91" stroke-width="1"/>
    </g>
  </svg>
  <div class="community" style="left:22px"><h3 class="current">STONEBRIDGE</h3><p>A ranch-inspired neighborhood in Prineville with open views, trails and room to breathe.</p><div class="more">Read More &#9656;</div></div>
  <div class="community" style="left:204px;width:188px"><h3>SUMMIT PINES VILLAGE RESORT</h3><p>Resort lodging near the mountain with pools, tennis and easy access to the river trail.</p><div class="more">Read More &#9656;</div></div>
  <div class="community" style="left:395px"><h3>CANYON RIM</h3><p>Homesites along the canyon edge with sweeping views of the Cascades and the river.</p><div class="more">Read More &#9656;</div></div>
  <div class="community" style="left:578px"><h3>WESTFIELD COMMONS</h3><p>A walkable neighborhood with parks, shops and schools close to downtown Bend.</p><div class="more">Read More &#9656;</div></div>
</section>

<section class="abs welcome">
  <h2>WELCOME TO HALVARD-HOLDINGS</h2>
  <p>Central Oregon real estate developer Halvard Holdings Corporation has created some of Central Oregon’s most recognizable real estate communities, including Westfield Commons, Canyon Rim, Riverbend, Juniper Butte, Juniper Glen, Summit Pines Village Resort, and Stonebridge in Prineville.</p>
  <span class="btn">READ MORE</span>
</section>

<section class="abs video" role="img" aria-label="Video still of a hand holding a solar panel">
  <h2>VIDEO</h2>
  <p>Take a short tour of our communities and see how we have shaped livable, healthy neighborhoods in Central Oregon for more than fifty years. Meet the people, places and trails that make this region a wonderful place to call home.</p>
  <span class="btn">VIEW ALL</span>
</section>
<svg class="abs play" width="56" height="56" viewBox="0 0 56 56">
  <circle cx="28" cy="28" r="25" fill="none" stroke="#8a8a8a" stroke-width="3.5"/>
  <polygon points="21,15 41,28 21,41" fill="#8a8a8a"/>
</svg>

<section class="abs recent">
  <h2>RECENT POST</h2>
  <div class="post">
    <div class="post-date">
      <div class="m">JAN</div>
      <svg class="wave" width="60" height="24" viewBox="0 0 60 24"><path d="M0,8 C15,-2 35,14 60,4 L60,24 L0,24 Z" fill="#f2f2f2"/></svg>
      <div class="y">2016</div>
    </div>
    <h4>DANIEL MARSH RETURNS TO HALVARD HOLDINGS AS PRESIDENT AND CEO</h4>
    <p>Halvard Holdings Corporation has hired Daniel Marsh as president and CEO for the company. A long-time employee of the company from 1993-2010, Marsh is returning to the real estate firm to provide leadership and work with the board and management &nbsp;&#10148;</p>
  </div>
</section>

<footer class="abs footer">
  <small>© All Rights Reserved. Copyrights @CompanyName .2016</small>
  <div class="social"><i></i><i></i><i></i><i></i><i></i></div>
</footer>

</body>
</html>
```